Photography Business Card Design

I want a simple,classy design using a logo and simple font such as minion pro or similar. I have attached a logo that I quite like or am open to something similar. On the back of the card I would like the attached photo possibly with my website address on it some where. I want a matt black with silver or grey print. Possibly have the logo off to one side with the words Daniel Festerby Photography stacked on top of each other
Updates
I am very sorry that some how I forgot to put my facebook address on the details section, www.socialpage.example/DanielFesterbyPhotography
If this could be include on the card as well.
Industry/Entity Type
Business
Contact Information for Business Card
Daniel Festerby Photography
www.danielfesterbyphotography.example.au
Email: danielfesterby@wirenest.example
Phone: +61 (0)427 318 502
Logo Text
Logo styles of interest
Abstract Logo
Look and feel

```html
<!DOCTYPE html>
<html lang="en">
<head>
<meta charset="utf-8">
<title>Daniel Festerby Photography – Business Card</title>
<link rel="stylesheet" href="https://fonts.googleapis.com/css2?family=Crimson+Pro:wght@400;600&display=swap">
<style>
  :root {
    --backdrop: #e6e7e9;
    --card-black: #050608;
    --print-grey: #5b5b5e;
    --card-shadow: rgba(0, 0, 0, 0.35);
  }
  * { margin: 0; padding: 0; box-sizing: border-box; }
  html, body {
    width: 1200px;
    height: 1000px;
    overflow: hidden;
    background: var(--backdrop);
  }
  body {
    position: relative;
    font-family: "Crimson Pro", "Minion Pro", Georgia, serif;
    color: var(--print-grey);
  }
  .card {
    position: absolute;
    width: 661px;
    height: 381px;
    background: var(--card-black);
    box-shadow: 4px 5px 6px var(--card-shadow);
  }
  .card--front { left: 70px; top: 94px; }
  .card--back  { left: 469px; top: 525px; }

  /* Wordmark stand-in */
  .wordmark {
    position: absolute;
    display: flex;
    align-items: center;
    font-weight: 600;
    line-height: 1.05;
    color: var(--print-grey);
  }
  .wordmark__square {
    background: var(--print-grey);
    flex: none;
  }
  .card--front .wordmark {
    left: 47px;
    top: 64px;
    font-size: 20px;
    gap: 12px;
  }
  .card--front .wordmark__square { width: 14px; height: 14px; }
  .card--back .wordmark {
    left: 0;
    right: 0;
    top: 110px;
    justify-content: center;
    font-size: 34px;
    gap: 20px;
  }
  .card--back .wordmark__square { width: 22px; height: 22px; }

  /* Front details */
  .business-name {
    position: absolute;
    left: 47px;
    top: 228px;
    font-size: 32px;
    font-weight: 600;
    letter-spacing: 0.1px;
  }
  .contact-list {
    position: absolute;
    left: 47px;
    top: 272px;
    list-style: none;
    font-size: 19px;
    font-weight: 400;
  }
  .contact-list li {
    display: flex;
    align-items: center;
    gap: 7px;
    height: 31px;
  }
  .contact-icon { width: 18px; height: 18px; flex: none; }

  /* Back */
  .website {
    position: absolute;
    left: 0;
    right: 0;
    top: 305px;
    text-align: center;
    font-size: 20px;
    font-weight: 400;
  }
</style>
</head>
<body>

  <section class="card card--front" aria-label="Business card front">
    <div class="wordmark">
      <span class="wordmark__square"></span>
      <span class="wordmark__name">Daniel Festerby<br>Photography</span>
    </div>

    <h1 class="business-name">Daniel Festerby Photography</h1>

    <ul class="contact-list">
      <li>
        <svg class="contact-icon" viewBox="0 0 18 18" aria-hidden="true">
          <rect x="1" y="1" width="16" height="16" rx="4" fill="var(--print-grey)"/>
          <path d="M5 9h8M12.5 6.2A4 4 0 1 0 12.5 11.8" stroke="var(--card-black)" stroke-width="1.8" fill="none"/>
        </svg>
        danielfesterby@wirenest.example
      </li>
      <li>
        <svg class="contact-icon" viewBox="0 0 18 18" aria-hidden="true">
          <path d="M5 2h3v4H6.5v6H8v4H5C3.5 14 3 11.5 3 9s.5-5 2-7z" fill="var(--print-grey)"/>
          <path d="M11 5c1.5 1 1.5 7 0 8" stroke="var(--print-grey)" stroke-width="1.6" fill="none"/>
        </svg>
        +61 (0)427 318 502
      </li>
    </ul>
  </section>

  <section class="card card--back" aria-label="Business card back">
    <div class="wordmark">
      <span class="wordmark__square"></span>
      <span class="wordmark__name">Daniel Festerby<br>Photography</span>
    </div>
    <p class="website">www.DanielFesterbyPhotography.example.au</p>
  </section>

</body>
</html>
```